Jewellery retailer needs a flyer design please

We need a flyer to represent our business.

Our company provides The lowest priced diamonds in Australia.
We are wholesales who sell direct to the public
We GENUINELY are 50-70% cheaper than other retail stores.

We guarantee the lowest prices, even in the unlikely event a customer finds a cheaper price than ours, we will beat it too.

Well tell our customers if youre not buying from us then you're paying too much.

Please include website www.amberloomstore.com.au
and facebook page www.facebook.com/mosslightcove.

We have location in Harbourgate Parramatta, and Harbourgate Liverpool, NSW.

Im sorry, this is the first time ive done this, so i hope ive given the information you need.

Target Market(s)

People wanting to buy engagement rings are our biggest customers.

Industry/Entity Type

Retail

Colors
276db0
3276b5
86acd3
cedeed

Requirements
Must have
• Simple, to the point! We need people to know that we have the lowest prices without compromising on quality
Nice to have
• I am very very open to anything. I do not have any particular expectations

```html
<!DOCTYPE html>
<html lang="en">
<head>
<meta charset="utf-8">
<title>Amberloom – Wholesale Diamonds Flyer</title>
<link rel="stylesheet" href="https://fonts.googleapis.com/css2?family=Rosario:wght@400;700&family=Satisfy&family=Open+Sans:wght@400;600&display=swap">
<style>
  :root {
    --stage: #f1f2f3;
    --paper: #ffffff;
    --blue-deep: #276db0;
    --blue-mid: #3276b5;
    --blue-soft: #86acd3;
    --blue-pale: #cedeed;
    --ink: #1f3558;
    --ring: #d9e4f1;
    --rose: #f4c9cf;
    --rose-pale: #fbe7ea;
  }
  * { box-sizing: border-box; margin: 0; padding: 0; }
  html, body { width: 1200px; height: 1000px; overflow: hidden; }
  body {
    background: var(--stage);
    font-family: "Rosario", "Trebuchet MS", sans-serif;
    position: relative;
  }
  .flyer {
    position: absolute;
    left: 313px; top: 92px;
    width: 575px; height: 816px;
    background: var(--paper);
    overflow: hidden;
  }
  .offer-ribbon {
    position: absolute; left: 27px; top: 0;
    width: 123px; height: 176px;
  }
  .offer-ribbon .label {
    position: absolute; left: 0; top: 12px; width: 123px;
    text-align: center; color: #fff;
    font-family: "Open Sans", Arial, sans-serif;
    font-size: 25px; line-height: 1.36;
  }
  .offer-ribbon .label strong { font-weight: 600; font-size: 29px; }
  .brand {
    position: absolute; left: 367px; top: 63px; width: 180px; height: 36px;
    display: flex; align-items: center; justify-content: center; gap: 10px;
    color: var(--ink); font-family: "Rosario", sans-serif;
    font-size: 28px; line-height: 36px;
  }
  .brand .dot {
    width: 12px; height: 12px; border-radius: 50%; background: var(--blue-soft);
  }
  .brand-rule {
    position: absolute; left: 367px; width: 180px; height: 1px; background: var(--ink); opacity: .6;
  }
  .brand-rule.top { top: 58px; }
  .brand-rule.bottom { top: 103px; left: 380px; width: 154px; }
  .photo-roses {
    position: absolute; left: 307px; top: 288px; width: 268px; height: 227px;
    background: radial-gradient(ellipse at 65% 65%, var(--rose) 0%, #f7d8dc 45%, var(--rose-pale) 75%, #fff 100%);
  }
  .photo-hands {
    position: absolute; left: 155px; top: 96px; width: 320px; height: 320px;
    border-radius: 50%;
    border: 6px solid #fff;
    box-shadow: 0 0 0 3px var(--ring), 0 0 10px rgba(134,172,211,.4);
    background: radial-gradient(circle at 45% 55%, #eccfc4 0%, #e3c1b6 35%, #dce8f1 70%, #eef3f8 100%);
  }
  .photo-ring {
    position: absolute; left: 33px; top: 301px; width: 194px; height: 194px;
    border-radius: 50%;
    border: 6px solid #fff;
    box-shadow: 0 0 0 3px var(--ring), 0 0 10px rgba(134,172,211,.4);
    background: radial-gradient(circle at 50% 50%, #d8dde3 0%, #eef0f3 50%, #fff 100%);
  }
  .sparkle { position: absolute; }
  .info-band {
    position: absolute; left: 0; top: 515px; width: 575px; height: 301px;
    background: linear-gradient(180deg, var(--blue-soft) 0%, #a9c4e1 55%, var(--blue-pale) 100%);
    text-align: center; color: var(--ink);
  }
  .headline {
    font-family: "Satisfy", "Brush Script MT", cursive;
    color: #fff; font-size: 36px; line-height: 40px; font-weight: 400;
    margin-top: 30px;
    text-shadow: 0 1px 3px rgba(31,53,88,.45);
  }
  .pitch { margin-top: 22px; font-size: 14px; line-height: 20px; }
  .call { margin-top: 14px; font-size: 16px; }
  .call strong { font-weight: 700; }
  .contact { margin-top: 16px; font-size: 12px; line-height: 20px; }
  .contact .sep { margin: 0 6px; }
</style>
</head>
<body>
  <main class="flyer">
    <div class="offer-ribbon">
      <svg width="123" height="176" viewBox="0 0 123 176" aria-hidden="true">
        <defs>
          <linearGradient id="ribbonFill" x1="0" y1="0" x2="1" y2="0">
            <stop offset="0" stop-color="#9ab9dc"/>
            <stop offset="1" stop-color="#86acd3"/>
          </linearGradient>
        </defs>
        <path d="M0 0 H123 V176 L61.5 152 L0 176 Z" fill="url(#ribbonFill)"/>
        <path d="M9 0 V150" stroke="#fff" stroke-width="1.5" stroke-dasharray="6 5"/>
        <path d="M114 0 V150" stroke="#fff" stroke-width="1.5" stroke-dasharray="6 5"/>
        <path d="M9 158 L61.5 140 L114 158" fill="none" stroke="#fff" stroke-width="1.5" stroke-dasharray="6 5"/>
      </svg>
      <div class="label">Upto<br><strong>70%</strong><br>OFF</div>
    </div>

    <div class="brand-rule top"></div>
    <div class="brand"><span class="dot"></span>Amberloom</div>
    <div class="brand-rule bottom"></div>

    <div class="photo-roses" role="img" aria-label="Bouquet of pale pink roses"></div>
    <div class="photo-hands" role="img" aria-label="Close-up of two clasped hands with a diamond engagement ring"></div>
    <div class="photo-ring" role="img" aria-label="Platinum diamond engagement ring with matching band"></div>

    <svg class="sparkle" style="left:433px;top:163px" width="60" height="60" viewBox="-30 -30 60 60" aria-hidden="true">
      <path d="M0 -30 L3 -3 L30 0 L3 3 L0 30 L-3 3 L-30 0 L-3 -3 Z" fill="#86acd3"/>
    </svg>

    <section class="info-band">
      <h1 class="headline">Wholesale diamonds with<br>Sparkling discounts</h1>
      <p class="pitch">We offer the finest quality diamonds in various cuts, colours and designs<br>in unbeatable prices, because we want to show that you are special.<br>We challenge you to find a price that is cheaper than ours.</p>
      <p class="call">So come over, <strong>Indulge</strong>.</p>
      <p class="contact">Harbourgate Parramatta and Harbourgate Liverpool, NSW.<br>www.amberloomstore.com.au<span class="sep">|</span>www.facebook.com/mosslightcove</p>
    </section>

    <svg class="sparkle" style="left:518px;top:534px" width="30" height="30" viewBox="-15 -15 30 30" aria-hidden="true">
      <path d="M0 -15 L1.5 -1.5 L15 0 L1.5 1.5 L0 15 L-1.5 1.5 L-15 0 L-1.5 -1.5 Z" fill="#fff"/>
    </svg>
    <svg class="sparkle" style="left:76px;top:552px" width="14" height="14" viewBox="-7 -7 14 14" aria-hidden="true">
      <path d="M0 -7 L1 -1 L7 0 L1 1 L0 7 L-1 1 L-7 0 L-1 -1 Z" fill="#fff"/>
    </svg>
    <svg class="sparkle" style="left:25px;top:645px" width="30" height="30" viewBox="-15 -15 30 30" aria-hidden="true">
      <path d="M0 -15 L1.5 -1.5 L15 0 L1.5 1.5 L0 15 L-1.5 1.5 L-15 0 L-1.5 -1.5 Z" fill="#fff"/>
    </svg>
    <svg class="sparkle" style="left:518px;top:746px" width="30" height="30" viewBox="-15 -15 30 30" aria-hidden="true">
      <path d="M0 -15 L1.5 -1.5 L15 0 L1.5 1.5 L0 15 L-1.5 1.5 L-15 0 L-1.5 -1.5 Z" fill="#fff"/>
    </svg>
    <svg class="sparkle" style="left:17px;top:762px" width="16" height="16" viewBox="-8 -8 16 16" aria-hidden="true">
      <path d="M0 -8 L1 -1 L8 0 L1 1 L0 8 L-1 1 L-8 0 L-1 -1 Z" fill="#fff"/>
    </svg>
  </main>
</body>
</html>
```